Travinex - You are the Boss!

Travinex is a new Silicon Valley company, of the pelim founders from Berlin, which provides a "Shared Pioneer Circle". This platform allows the crowd to support startups with money, experts and fame. Our Vision is, that everyone should become an entrepreneur.

Pls find all brief details in the attached document
Updates

Would be nice to have a list of more social services I'm available on, like a list of pictograms of all my services:

Find me on: vooka, bramlet+, qrt, fenwix, moodrail, zupp, hvoxa, etc...

pls make sure to use the right font:
http://www.typemarlow.com/fonts/Velquin

Target Market(s)

Main target market is those already involved in the startup industry, by fundraising, investing, advising, cofounding and working. Travinex brings a totaly new transparency and collaborative way of starting companies to that business.

· Entrepreneurs (looking for funding, team and community)
· Investors (looking for hot investments and )
· Experts (workers looking for startups they can work for equity)
· Incubators & Business Schools (looking for tools to advise startups)

Industry/Entity Type

It Company

Requirements
Must have
• Pls find all brief details in the attached document
Nice to have

```html
<!DOCTYPE html>
<html lang="en">
<head>
<meta charset="utf-8">
<title>Travinex Business Card</title>
<link rel="stylesheet" href="https://fonts.googleapis.com/css2?family=Orbitron:wght@700&family=Arimo:wght@400;700&family=Questrial&display=swap">
<style>
  :root {
    --backdrop: #383431;
    --card-white: #ffffff;
    --brand-orange: #e25d3b;
    --ink-grey: #8a8a8a;
    --label-grey: #8c8884;
    --text-light: #ffffff;
    --dash: #f3b3a1;
  }
  * { margin: 0; padding: 0; box-sizing: border-box; }
  html, body { width: 834px; height: 1200px; overflow: hidden; }
  body {
    background: var(--backdrop);
    font-family: "Arimo", Arial, sans-serif;
    position: relative;
  }
  .card {
    position: absolute;
    left: 97px;
    width: 640px;
    height: 370px;
  }
  .card-front { top: 157px; background: var(--card-white); }
  .card-back { top: 660px; background: var(--brand-orange); color: var(--text-light); text-align: center; }

  .brand-panel {
    position: absolute;
    left: 58px;
    top: 0;
    width: 218px;
    height: 249px;
    background: var(--brand-orange);
    border-radius: 0 0 24px 24px;
    color: var(--text-light);
    text-align: center;
  }
  .brand-name {
    position: absolute;
    left: 0; right: 0;
    top: 158px;
    font-family: "Arimo", Arial, sans-serif;
    font-size: 28px;
    font-weight: 400;
    line-height: 1;
  }

  .person-name {
    position: absolute;
    left: 303px;
    top: 151px;
    font-family: "Orbitron", Arial, sans-serif;
    font-weight: 700;
    font-size: 24px;
    letter-spacing: 1.6px;
    line-height: 30px;
    color: var(--brand-orange);
  }
  .person-role {
    position: absolute;
    left: 303px;
    top: 184px;
    font-size: 16px;
    font-weight: 700;
    line-height: 20px;
    color: var(--ink-grey);
  }
  .contact-line {
    position: absolute;
    left: 0; right: 0;
    top: 306px;
    text-align: center;
    font-family: "Questrial", Arial, sans-serif;
    font-size: 12.5px;
    color: var(--ink-grey);
  }
  .social-line {
    position: absolute;
    left: 0; right: 0;
    top: 326px;
    display: flex;
    justify-content: center;
    gap: 12px;
    font-family: "Questrial", Arial, sans-serif;
    font-size: 11px;
    color: var(--ink-grey);
  }
  .social-item { display: flex; align-items: center; gap: 9px; }
  .social-mark { width: 9px; height: 9px; background: var(--ink-grey); display: inline-block; }

  .side-label {
    position: absolute;
    left: 0; right: 0;
    text-align: center;
    font-size: 20px;
    color: var(--label-grey);
    line-height: 24px;
  }
  .label-front { top: 564px; }
  .label-back { top: 1067px; }

  .back-heading {
    position: absolute;
    left: 0; right: 0;
    top: 120px;
    font-size: 18px;
    font-weight: 700;
    line-height: 22px;
  }
  .back-join {
    position: absolute;
    left: 0; right: 0;
    top: 142px;
    font-size: 17px;
    line-height: 22px;
  }
  .back-divider {
    position: absolute;
    left: 118px;
    top: 285px;
    width: 400px;
    border-top: 1px dashed var(--dash);
  }
  .back-address {
    position: absolute;
    left: 0; right: 0;
    top: 305px;
    font-size: 12px;
    line-height: 15px;
  }
</style>
</head>
<body>
  <section class="card card-front">
    <div class="brand-panel">
      <div class="brand-name">Travinex</div>
    </div>
    <h1 class="person-name">MARTEN OSWALD</h1>
    <p class="person-role">FOUNDER AND CEO</p>
    <p class="contact-line">084 210 735 618 | www.travinex.com | mos@travinex.com</p>
    <div class="social-line">
      <span class="social-item"><span class="social-mark"></span>chirpa.com/martenoswald</span>
      <span class="social-item"><span class="social-mark"></span>facelink.com/martenoswald</span>
      <span class="social-item"><span class="social-mark"></span>prolinq.com/in/martenoswald</span>
    </div>
  </section>
  <div class="side-label label-front">FRONT</div>

  <section class="card card-back">
    <p class="back-heading">Are you interested in Startups, Investments, Work?</p>
    <p class="back-join">Join: Facelink.com/Travinex</p>
    <div class="back-divider"></div>
    <p class="back-address">Berlin - Lindenhof Strasse 24 . 10117 Berlin . Germany<br>Silicon Valley - 218 Orchard Ave . Sunnyvale . CA 94086</p>
  </section>
  <div class="side-label label-back">BACK</div>
</body>
</html>
```